Flyer for Home Improvement Lead Generation

We need a flyer that shows people the work we do. Replacement windows doors and siding. We offer quality products and great workmanship at fair prices. The company name is Granite Ridge Remodeling. I will upload a document with some of the features we would like to show in the flyer.
Wow would like to keep a homegrown look to our marketing.
We use Georgia font in caps for our logo text.
The hex for the logo color is #F67B04
This flyer will be for lead generation so it should showcase reasons to call us.
Our web address. grr-vt.com
Our Phone number. 860-412-9368
leave a spot for a QR code.
Target Market(s)
Residential
Industry/Entity Type
Home Improvement. Replacement windows, doors and siding
Look and feel

```html
<!DOCTYPE html>
<html lang="en">
<head>
<meta charset="UTF-8">
<title>Granite Ridge Remodeling – What Do You Get</title>
<link href="https://fonts.googleapis.com/css2?family=Source+Sans+3:wght@600;700;800;900&display=swap" rel="stylesheet">
<style>
  :root {
    --ink: #0a0a0a;
    --flame: #f67b04;
    --paper: #ffffff;
  }
  html, body {
    margin: 0;
    padding: 0;
    width: 1200px;
    height: 2700px;
    overflow: hidden;
    background: var(--ink);
  }
  .flyer {
    position: relative;
    width: 1200px;
    height: 2700px;
    background: var(--ink);
    color: var(--paper);
    font-family: "Source Sans 3", Arial, sans-serif;
  }
  .headline {
    position: absolute;
    top: 96px;
    left: 0;
    width: 1200px;
    margin: 0;
    text-align: center;
    font-family: "Source Sans 3", Arial, sans-serif;
    font-weight: 800;
    font-size: 118px;
    line-height: 130px;
    letter-spacing: -1px;
    color: var(--flame);
  }
  .benefits {
    list-style: none;
    margin: 0;
    padding: 0;
  }
  .benefit {
    position: absolute;
    left: 0;
    width: 1200px;
    height: 200px;
  }
  .benefit-check {
    position: absolute;
    left: 144px;
    top: 26px;
    width: 112px;
    height: 112px;
    overflow: visible;
  }
  .benefit-text {
    position: absolute;
    left: 354px;
    top: 0;
    width: 760px;
    margin: 0;
    font-weight: 600;
    font-size: 38px;
    line-height: 50px;
    color: var(--paper);
  }
  .brand-block {
    position: absolute;
    top: 2262px;
    left: 144px;
    width: 740px;
  }
  .brand {
    margin: 0;
    font-family: Georgia, "Times New Roman", serif;
    font-weight: 400;
    font-size: 40px;
    line-height: 56px;
    letter-spacing: 1px;
    text-transform: uppercase;
    color: var(--flame);
  }
  .web {
    margin: 14px 0 0;
    font-weight: 600;
    font-size: 36px;
    line-height: 46px;
    color: var(--paper);
  }
  .qr-spot {
    position: absolute;
    top: 2240px;
    left: 916px;
    width: 160px;
    height: 160px;
    background: var(--paper);
  }
  .phone {
    position: absolute;
    top: 2470px;
    left: 0;
    width: 1200px;
    text-align: center;
    font-family: "Source Sans 3", Arial, sans-serif;
    font-weight: 800;
    font-size: 150px;
    line-height: 170px;
    color: var(--paper);
  }
</style>
</head>
<body>
<main class="flyer">
  <h1 class="headline">WHAT DO YOU GET</h1>

  <ul class="benefits">
    <li class="benefit" style="top:258px">
      <svg class="benefit-check" viewBox="0 0 112 112"><rect x="4" y="4" width="104" height="104" fill="none" stroke="#ffffff" stroke-width="8"/><polyline points="30,54 58,84 118,0" fill="none" stroke="#f67b04" stroke-width="16" stroke-linecap="square"/></svg>
      <p class="benefit-text">Increased energy efficiency,<br>leading to potential cost savings<br>on heating and cooling bills.</p>
    </li>
    <li class="benefit" style="top:458px">
      <svg class="benefit-check" viewBox="0 0 112 112"><rect x="4" y="4" width="104" height="104" fill="none" stroke="#ffffff" stroke-width="8"/><polyline points="30,54 58,84 118,0" fill="none" stroke="#f67b04" stroke-width="16" stroke-linecap="square"/></svg>
      <p class="benefit-text">Enhanced curb appeal,<br>improving the overall appearance<br>&nbsp;and value of your home.</p>
    </li>
    <li class="benefit" style="top:658px">
      <svg class="benefit-check" viewBox="0 0 112 112"><rect x="4" y="4" width="104" height="104" fill="none" stroke="#ffffff" stroke-width="8"/><polyline points="30,54 58,84 118,0" fill="none" stroke="#f67b04" stroke-width="16" stroke-linecap="square"/></svg>
      <p class="benefit-text">Better insulation, resulting in improved<br>comfort levels and reduced noise from<br>outside.</p>
    </li>
    <li class="benefit" style="top:858px">
      <svg class="benefit-check" viewBox="0 0 112 112"><rect x="4" y="4" width="104" height="104" fill="none" stroke="#ffffff" stroke-width="8"/><polyline points="30,54 58,84 118,0" fill="none" stroke="#f67b04" stroke-width="16" stroke-linecap="square"/></svg>
      <p class="benefit-text">Enhanced security features, providing<br>peace of mind and protection for your<br>family and belongings.</p>
    </li>
    <li class="benefit" style="top:1058px">
      <svg class="benefit-check" viewBox="0 0 112 112"><rect x="4" y="4" width="104" height="104" fill="none" stroke="#ffffff" stroke-width="8"/><polyline points="30,54 58,84 118,0" fill="none" stroke="#f67b04" stroke-width="16" stroke-linecap="square"/></svg>
      <p class="benefit-text">Reduced maintenance<br>requirements, saving time<br>and effort on upkeep.</p>
    </li>
    <li class="benefit" style="top:1258px">
      <svg class="benefit-check" viewBox="0 0 112 112"><rect x="4" y="4" width="104" height="104" fill="none" stroke="#ffffff" stroke-width="8"/><polyline points="30,54 58,84 118,0" fill="none" stroke="#f67b04" stroke-width="16" stroke-linecap="square"/></svg>
      <p class="benefit-text">Improved functionality<br>and ease of use,<br>with modern designs and features.</p>
    </li>
    <li class="benefit" style="top:1458px">
      <svg class="benefit-check" viewBox="0 0 112 112"><rect x="4" y="4" width="104" height="104" fill="none" stroke="#ffffff" stroke-width="8"/><polyline points="30,54 58,84 118,0" fill="none" stroke="#f67b04" stroke-width="16" stroke-linecap="square"/></svg>
      <p class="benefit-text">Potential increase in resale value,<br>making your home more attractive<br>to potential buyers.</p>
    </li>
    <li class="benefit" style="top:1658px">
      <svg class="benefit-check" viewBox="0 0 112 112"><rect x="4" y="4" width="104" height="104" fill="none" stroke="#ffffff" stroke-width="8"/><polyline points="30,54 58,84 118,0" fill="none" stroke="#f67b04" stroke-width="16" stroke-linecap="square"/></svg>
      <p class="benefit-text">Customization options<br>to match your personal style<br>and preferences.</p>
    </li>
    <li class="benefit" style="top:1858px">
      <svg class="benefit-check" viewBox="0 0 112 112"><rect x="4" y="4" width="104" height="104" fill="none" stroke="#ffffff" stroke-width="8"/><polyline points="30,54 58,84 118,0" fill="none" stroke="#f67b04" stroke-width="16" stroke-linecap="square"/></svg>
      <p class="benefit-text">Protection against the elements,<br>including weather resistance<br>and durability.</p>
    </li>
    <li class="benefit" style="top:2058px">
      <svg class="benefit-check" viewBox="0 0 112 112"><rect x="4" y="4" width="104" height="104" fill="none" stroke="#ffffff" stroke-width="8"/><polyline points="30,54 58,84 118,0" fill="none" stroke="#f67b04" stroke-width="16" stroke-linecap="square"/></svg>
      <p class="benefit-text">Potential eligibility for energy efficiency<br>incentives or tax credits, leading to<br>additional savings.</p>
    </li>
  </ul>

  <div class="brand-block">
    <p class="brand">Granite Ridge Remodeling</p>
    <p class="web">grr-vt.com</p>
  </div>
  <div class="qr-spot" role="img" aria-label="Space reserved for QR code"></div>

  <div class="phone">860-412-9368</div>
</main>
</body>
</html>
```